Business Card Design Project

We need a business card for our new business based in Vancouver called
"Lumora Haven" We are looking for a simple yet bold design for our business cards that will enable us to stand out from the pack. All business card details will be provided in the handover stage.
Updates

Thank you to all who have submitted

The work is great for the most part
Cards with creative use of the logo
have been more successful so far

Dark cards and rounded edges 
are also getting good reviews

Double sided is an option we would like to see explored

Thank you

Target Market(s)

Our clients are stressed business people, yoga/meditation enthusiast, and people looking for a new experience in a Spa enviroment

Industry/Entity Type

Business

Font styles to use
Other font styles liked:
• please check design file

Requirements
Must have
• Lumora Haven

5218 E Kestrel Row, Vancouver, BC V5N 4K7

lumora@calmhaven.ca
Nice to have
• Creative approach to layout and design

Outside of the box design elements
Should not have
• Should not be too busy

```html
<!DOCTYPE html>
<html lang="en">
<head>
<meta charset="UTF-8">
<title>Lumora Haven – Business Card</title>
<link rel="stylesheet" href="https://fonts.googleapis.com/css2?family=Dosis:wght@300;400&display=swap">
<style>
  :root {
    --sky: #a9dcf5;
    --periwinkle: #a7c1e8;
    --lavender: #c6c6ea;
    --mist: #f2f4f8;
    --brand-ink: #3b2a86;
    --text-grey: #7b7b86;
  }
  * { margin: 0; padding: 0; box-sizing: border-box; }
  html, body {
    width: 1200px;
    height: 686px;
    overflow: hidden;
    background: #ffffff;
  }
  .card {
    position: relative;
    width: 1200px;
    height: 686px;
    overflow: hidden;
    font-family: "Dosis", sans-serif;
  }
  .card__backdrop {
    position: absolute;
    inset: 0;
    background:
      radial-gradient(ellipse 600px 340px at 470px 290px, var(--mist) 0%, rgba(242,244,248,0.85) 45%, rgba(242,244,248,0) 100%),
      linear-gradient(90deg, var(--sky) 0%, var(--periwinkle) 35%, var(--lavender) 55%, var(--periwinkle) 75%, var(--lavender) 100%);
  }
  .brand {
    position: absolute;
    left: 108px;
    top: 118px;
    height: 226px;
    display: flex;
    align-items: center;
    gap: 70px;
  }
  .brand__mark {
    flex: none;
    width: 226px;
    height: 226px;
    border: 3px solid var(--brand-ink);
    border-radius: 50%;
  }
  .brand__name {
    color: var(--brand-ink);
    font-weight: 300;
    font-size: 104px;
    line-height: 1;
    white-space: nowrap;
  }
  .contact {
    position: absolute;
    left: 103px;
    color: var(--text-grey);
    font-weight: 400;
    line-height: 1;
    white-space: nowrap;
  }
  .contact--address {
    top: 386px;
    font-size: 59px;
  }
  .contact--email {
    top: 480px;
    font-size: 47px;
  }
</style>
</head>
<body>
  <main class="card">
    <div class="card__backdrop" role="img" aria-label="Soft pale blue and lavender wave background with a white glow behind the brand"></div>

    <header class="brand">
      <div class="brand__mark"></div>
      <h1 class="brand__name">Lumora Haven</h1>
    </header>

    <p class="contact contact--address">5218 E Kestrel Row, Vancouver, BC V5N 4K7</p>
    <p class="contact contact--email">lumora@calmhaven.ca</p>
  </main>
</body>
</html>
```